Marlowen

I'm looking for business cards with the logo I've attached. I don't have an specific idea in mind and open to anything. All the usual info will be involved. Name, position in company, nr, email, address

```html
<!DOCTYPE html>
<html lang="en">
<head>
<meta charset="utf-8">
<title>Marlowen Designs — Business Cards</title>
<link href="https://fonts.googleapis.com/css2?family=Inter:wght@400;600&display=swap" rel="stylesheet">
<style>
  :root {
    --backdrop: #1e1f22;
    --card-navy: #13284a;
    --accent-gold: #f2ac1c;
    --text-white: #f4f6fa;
    --divider: rgba(244, 246, 250, 0.75);
  }
  * { margin: 0; padding: 0; box-sizing: border-box; }
  html, body {
    width: 1200px;
    height: 874px;
    overflow: hidden;
    background: var(--backdrop);
    font-family: "Inter", Arial, sans-serif;
  }
  .card-set {
    position: absolute;
    left: 290px;
    top: 62px;
    width: 620px;
    display: flex;
    flex-direction: column;
    gap: 30px;
  }
  .card {
    width: 620px;
    height: 355px;
    background: var(--card-navy);
    position: relative;
    box-shadow: 0 10px 24px rgba(0, 0, 0, 0.45);
  }
  /* Front */
  .card-front {
    display: flex;
    align-items: center;
    justify-content: center;
  }
  .brand {
    display: flex;
    align-items: center;
    gap: 16px;
    color: var(--accent-gold);
    font-weight: 600;
  }
  .brand-dot {
    width: 22px;
    height: 22px;
    border-radius: 50%;
    background: var(--accent-gold);
  }
  .brand-name {
    font-size: 44px;
    letter-spacing: 2px;
    line-height: 1;
    text-transform: uppercase;
  }
  /* Back */
  .card-back .contact-block {
    position: absolute;
    left: 0;
    right: 0;
    top: 176px;
    display: flex;
    justify-content: center;
    padding-right: 40px;
  }
  .identity {
    text-align: right;
    padding-right: 16px;
    color: var(--text-white);
    font-size: 15px;
    line-height: 1.25;
  }
  .identity .person-name {
    color: var(--accent-gold);
    font-weight: 600;
    font-size: 20px;
    letter-spacing: 0.3px;
    margin-bottom: 3px;
  }
  .divider {
    width: 1px;
    background: var(--divider);
    align-self: stretch;
    margin-top: 10px;
    height: 104px;
  }
  .contact-list {
    list-style: none;
    padding-left: 16px;
    padding-top: 40px;
    color: var(--text-white);
    font-size: 15px;
    line-height: 1.32;
  }
  .contact-list li {
    display: flex;
    align-items: center;
    gap: 9px;
  }
  .contact-list svg {
    width: 12px;
    height: 12px;
    flex: none;
    fill: var(--accent-gold);
  }
</style>
</head>
<body>
  <main class="card-set">
    <section class="card card-front" aria-label="Card front">
      <div class="brand">
        <span class="brand-dot"></span>
        <span class="brand-name">Marlowen Designs</span>
      </div>
    </section>

    <section class="card card-back" aria-label="Card back">
      <div class="contact-block">
        <div class="identity">
          <p class="person-name">DANIEL HARROW</p>
          <p>President</p>
          <p>4120 Birchwood Court</p>
          <p>Fairbanks, Alaska 99712</p>
        </div>
        <span class="divider"></span>
        <ul class="contact-list">
          <li>
            <svg viewBox="0 0 12 12" aria-hidden="true"><path d="M2.5 0.5 L4.5 2.8 L3.4 4.2 C4.1 5.8 6.2 7.9 7.8 8.6 L9.2 7.5 L11.5 9.5 L10 11.5 C5 11 1 7 0.5 2 Z"/></svg>
            555-214-7730
          </li>
          <li>
            <svg viewBox="0 0 12 12" aria-hidden="true"><path d="M3 0 H9 V12 H3 Z M4 1.5 V9.5 H8 V1.5 Z"/></svg>
            555-318-6042
          </li>
          <li>
            <svg viewBox="0 0 12 12" aria-hidden="true"><path d="M0 2 H12 V10 H0 Z M1 3 L6 6.8 L11 3 Z"/></svg>
            hello@marlowendesigns.com
          </li>
          <li>
            <svg viewBox="0 0 12 12" aria-hidden="true"><circle cx="6" cy="6" r="6"/><path d="M1 6 H11 M6 0.5 V11.5" stroke="#13284a" stroke-width="1"/></svg>
            www.marlowendesigns.com
          </li>
        </ul>
      </div>
    </section>
  </main>
</body>
</html>
```